Faithful in the Small...Powerful together

Capital Campaign for Meadowlight Church...need it engaging..spiritually based with pics of the community etc...

Target Market(s)

church congregation and sphere of influence

Industry/Entity Type

religious

Colors
EB3D1F
EC4F4E
F09395
F8D3D4
FCEDEE

Requirements
Must have
• tier levels..engaging scripture and photos

```html
<!DOCTYPE html>
<html lang="en">
<head>
<meta charset="utf-8">
<title>Meadowlight Church – Capital Campaign Brochure</title>
<link href="https://fonts.googleapis.com/css2?family=Poppins:wght@400;500;600;700&family=Montserrat:wght@400;600;700&family=Mr+Dafoe&family=Allura&display=swap" rel="stylesheet">
<style>
:root{
  --red:#EB3D1F;
  --brand-red:#E31E26;
  --coral:#EC4F4E;
  --rose:#F09395;
  --blush:#F8D3D4;
  --mist:#FCEDEE;
  --ink:#1d1d1d;
  --stage:#5f5f5f;
  --white:#ffffff;
  --charcoal:#2b2b2b;
}
*{margin:0;padding:0;box-sizing:border-box}
html,body{width:808px;height:1200px;overflow:hidden}
body{background:var(--stage);font-family:"Montserrat",sans-serif;color:var(--ink);position:relative}
.panel-label{position:absolute;font-family:"Poppins",sans-serif;font-weight:500;color:var(--white);font-size:23px;transform:translateX(-50%);white-space:nowrap}
.spread{position:absolute;left:79px;width:650px;height:459px;background:var(--white);display:flex}
.spread-outside{top:108px}
.spread-inside{top:673px}
.panel{position:relative;width:325px;height:100%;overflow:hidden}
.abs{position:absolute}
.photo{position:absolute}
.goal-badge{position:absolute;display:flex;height:24px;border-radius:3px;overflow:hidden;font-family:"Poppins",sans-serif;font-size:12.5px;white-space:nowrap}
.goal-badge .goal-key{background:var(--rose);color:var(--ink);font-weight:600;padding:0 5px;display:flex;align-items:center}
.goal-badge .goal-val{background:var(--brand-red);color:var(--white);padding:0 6px;display:flex;align-items:center}
.goal-badge b{font-weight:700}
.contact-line{position:absolute;display:flex;align-items:center;gap:20px;white-space:nowrap}
.contact-phone{display:flex;align-items:center;gap:5px;font-family:"Poppins",sans-serif;font-weight:600;font-size:10px}
.contact-web{display:flex;align-items:center;gap:5px;font-size:6.5px}
.footer-band{position:absolute;left:0;bottom:4px;width:100%;height:20px;background:var(--brand-red);color:var(--white);display:flex;justify-content:center;align-items:center}
.footer-band::after{content:"";position:absolute;left:0;right:0;top:20px;height:4px;background:var(--ink)}
.section-title{font-family:"Poppins",sans-serif;font-weight:600;color:var(--brand-red);font-size:11.5px;text-align:center}
.script{font-family:"Allura",cursive;color:var(--coral);font-size:20px;line-height:1}
.body-text{font-size:6.3px;line-height:1.32}
.red{color:var(--brand-red)}
.tiers{border-collapse:collapse;width:297px;font-size:6.5px}
.tiers th,.tiers td{border:0.6px solid #9a7c7d;text-align:center;padding:0 6px}
.tiers th{background:var(--blush);height:27px;font-family:"Poppins",sans-serif;font-weight:600}
.tiers td{height:27px;background:rgba(255,255,255,.78)}
.tiers td:first-child,.tiers th:first-child{text-align:left;padding-left:13px}
.bullets{list-style:none}
.bullets li{position:relative;padding-left:7px;font-weight:700;font-size:6.4px;line-height:1.45}
.bullets li::before{content:"";position:absolute;left:0;top:3px;width:3px;height:3px;background:var(--brand-red)}
</style>
</head>
<body>

<div class="panel-label" style="left:247px;top:56px">Back</div>
<div class="panel-label" style="left:569px;top:56px">Front</div>
<div class="panel-label" style="left:247px;top:608px">Inside-1</div>
<div class="panel-label" style="left:569px;top:608px">Inside-2</div>

<section class="spread spread-outside">

  <div class="panel panel-back">
    <svg class="abs" width="325" height="459" viewBox="0 0 325 459" style="left:0;top:0">
      <defs>
        <linearGradient id="kitchenTone" x1="0" y1="0" x2="0" y2="1">
          <stop offset="0" stop-color="#c0533f"/>
          <stop offset=".35" stop-color="#8a7a70"/>
          <stop offset=".7" stop-color="#b9b5b0"/>
          <stop offset="1" stop-color="#f1efed"/>
        </linearGradient>
        <radialGradient id="groupTone" cx=".45" cy=".6" r=".7">
          <stop offset="0" stop-color="#9c8a86"/>
          <stop offset=".55" stop-color="#6c5452"/>
          <stop offset="1" stop-color="#231c1c"/>
        </radialGradient>
        <linearGradient id="swooshTone" x1="0" y1="0" x2="1" y2="0">
          <stop offset="0" stop-color="var(--brand-red)"/>
          <stop offset=".5" stop-color="#f3b5b7"/>
          <stop offset="1" stop-color="#f8d3d4"/>
        </linearGradient>
      </defs>
      <rect width="325" height="459" fill="#fff"/>
      <g role="img" aria-label="Photo of church volunteers serving food in the kitchen">
        <rect x="0" y="285" width="325" height="174" fill="url(#kitchenTone)"/>
      </g>
      <path d="M0 235 C60 320 200 330 325 250 L325 80 C280 180 170 260 0 235Z" fill="url(#swooshTone)"/>
      <g role="img" aria-label="Photo of smiling women from the congregation standing together">
        <path d="M0 0 L273 0 C330 80 330 190 250 260 C180 315 70 310 0 240Z" fill="url(#groupTone)"/>
      </g>
      <path d="M273 0 C330 80 330 190 250 260 C180 315 70 310 0 240" fill="none" stroke="#fff" stroke-width="2.5"/>
      <rect x="0" y="420" width="325" height="39" fill="#fff" opacity=".85"/>
    </svg>
    <div class="abs" style="left:122px;top:413px;background:var(--brand-red);color:#fff;font-family:'Poppins',sans-serif;font-weight:600;font-size:11px;padding:2px 9px;border-radius:3px">Contact Us</div>
    <div class="contact-line" style="left:62px;top:441px">
      <span class="contact-phone">
        <svg width="10" height="10" viewBox="0 0 24 24"><path d="M6.6 10.8a15 15 0 006.6 6.6l2.2-2.2a1 1 0 011-.25 11.4 11.4 0 003.6.6 1 1 0 011 1V20a1 1 0 01-1 1A17 17 0 013 4a1 1 0 011-1h3.5a1 1 0 011 1c0 1.25.2 2.45.6 3.6a1 1 0 01-.25 1z" fill="var(--ink)"/></svg>
        555.014.2290</span>
      <span class="contact-web">
        <svg width="9" height="9" viewBox="0 0 24 24" fill="none" stroke="var(--ink)" stroke-width="2"><circle cx="12" cy="12" r="10"/><path d="M2 12h20M12 2c3 3 3 17 0 20M12 2c-3 3-3 17 0 20"/></svg>
        www.meadowlight-church.org</span>
    </div>
  </div>

  <div class="panel panel-front">
    <svg class="abs" width="325" height="459" viewBox="0 0 325 459" style="left:0;top:0">
      <defs>
        <linearGradient id="pastorTone" x1="0" y1="0" x2="1" y2="1">
          <stop offset="0" stop-color="#8a8399"/>
          <stop offset=".45" stop-color="#8d6f97"/>
          <stop offset=".75" stop-color="#c9464f"/>
          <stop offset="1" stop-color="#e5303b"/>
        </linearGradient>
        <linearGradient id="prayerTone" x1="0" y1="0" x2="1" y2="1">
          <stop offset="0" stop-color="#2c3160"/>
          <stop offset=".5" stop-color="#8a6f80"/>
          <stop offset="1" stop-color="#d8cfd2"/>
        </linearGradient>
        <linearGradient id="bibleTone" x1="0" y1="0" x2="0" y2="1">
          <stop offset="0" stop-color="#ffffff"/>
          <stop offset=".55" stop-color="#fbeeee"/>
          <stop offset="1" stop-color="#efd9cf"/>
        </linearGradient>
        <linearGradient id="cornerTone" x1="1" y1="1" x2="0" y2="0">
          <stop offset="0" stop-color="#f6c9c9"/>
          <stop offset="1" stop-color="#f6c9c9" stop-opacity="0"/>
        </linearGradient>
      </defs>
      <g role="img" aria-label="Soft photo of an open Bible in warm light">
        <rect width="325" height="459" fill="url(#bibleTone)"/>
      </g>
      <g role="img" aria-label="Photo of the pastor preaching with hands raised">
        <path d="M0 0 H325 V243 H55 C30 240 10 235 0 230Z" fill="url(#pastorTone)"/>
      </g>
      <g role="img" aria-label="Photo of church members praying together">
        <rect x="152" y="152" width="173" height="91" fill="url(#prayerTone)"/>
      </g>
      <path d="M55 243 C100 230 140 222 152 225 L152 243Z" fill="var(--ink)"/>
      <path d="M150 0 C110 30 100 110 160 150 C220 175 300 165 325 155 V0Z" fill="var(--brand-red)"/>
      <path d="M165 0 C125 35 125 110 180 140 C230 160 300 155 325 150 V0Z" fill="#fff"/>
      <circle cx="303" cy="371" r="6" fill="#9a9a9a"/>
      <g role="img" aria-label="Soft decorative corner accent">
        <path d="M325 385 V459 H270Z" fill="url(#cornerTone)"/>
      </g>
    </svg>
    <div class="abs" style="left:190px;top:52px;width:130px;text-align:center;font-family:'Poppins',sans-serif;font-weight:600;color:var(--ink);font-size:15px;line-height:1.15">Meadowlight<br>Church</div>
    <div class="abs" style="left:0;top:262px;width:325px;text-align:center;font-family:'Mr Dafoe',cursive;font-size:34px;line-height:1.3">
      <div style="color:var(--ink)">Faithful in the Small,</div>
      <div style="color:var(--brand-red)">Powerful Together.</div>
    </div>
    <div class="goal-badge" style="left:67px;top:389px">
      <span class="goal-key">Goal:</span><span class="goal-val"><b>$150,000</b>&nbsp;in&nbsp;<b>12</b>&nbsp;Months</span>
    </div>
    <div class="contact-line" style="left:104px;top:434px">
      <span class="contact-web" style="font-size:7.5px">
        <svg width="9" height="9" viewBox="0 0 24 24" fill="none" stroke="var(--ink)" stroke-width="2"><circle cx="12" cy="12" r="10"/><path d="M2 12h20M12 2c3 3 3 17 0 20M12 2c-3 3-3 17 0 20"/></svg>
        www.meadowlight-church.org</span>
    </div>
  </div>
</section>

<section class="spread spread-inside">

  <div class="panel panel-inside-left">
    <div class="goal-badge" style="left:67px;top:19px">
      <span class="goal-key">Goal:</span><span class="goal-val"><b>$150,000</b>&nbsp;in&nbsp;<b>12</b>&nbsp;Months</span>
    </div>
    <div class="abs" style="left:15px;top:60px;width:297px;height:42px;border:1.2px solid var(--blush);display:flex;font-size:6.5px">
      <div style="width:175px;padding:8px 0 0 15px;line-height:1.4">
        <b>Total Goal:</b> <span class="red" style="font-weight:600">$150,000</span><br>
        <b>Active Members:</b> approximately <span class="red" style="font-weight:600">150</span> people<br>
        <b>Timeframe:</b> <span class="red" style="font-weight:600">12</span> months
      </div>
      <div style="flex:1;background:var(--mist);padding:13px 0 0 23px;line-height:1.3">
        That is <span class="red" style="font-weight:700">$1,000</span> per person<br>per year on average
      </div>
    </div>
    <div class="section-title abs" style="left:0;top:110px;width:325px">The Heart of the Vision</div>
    <div class="abs" style="left:29px;top:130px;width:268px;height:15px;display:flex;font-size:6.3px;font-weight:600">
      <div style="flex:1;background:var(--blush);display:flex;align-items:center;justify-content:center">We are restoring more than space</div>
      <div style="flex:1;background:var(--mist);display:flex;align-items:center;justify-content:center">We are restoring a church where we</div>
    </div>
    <div class="abs script" style="left:45px;top:158px;line-height:1.25">Love like Him<br><span style="color:var(--rose)">Live like Him</span><br>Lead like Him</div>
    <div class="abs" style="left:148px;top:166px;width:130px;font-size:6.3px;line-height:1.4">
      “Whoever is faithful in very little is also faithful in much.” <b class="red">Luke 16:10</b>
      <div style="height:1px;background:var(--coral);margin:8px 0 10px"></div>
      “How good and pleasant it is when God’s people live together in unity.” <b class="red">Psalm 133:1</b>
    </div>
    <div class="abs" style="left:0;top:245px;width:215px;height:170px;background:var(--blush);border-bottom-right-radius:22px">
      <div style="background:var(--mist);height:34px;padding:10px 0 0 15px;font-family:'Poppins',sans-serif;font-weight:600;color:var(--brand-red);font-size:11.5px">Stories of What God Is Doing</div>
      <div class="body-text" style="padding:10px 15px 0">
        <p>One Wednesday night, a woman went to visit another church, but they were closed for a break. Instead of turning back, she came here. That unexpected moment became a divine appointment. God brought her to Meadowlight.</p>
        <p style="margin-top:7px">Another couple walked through our doors carrying deep church hurt. From the very first moment, they felt seen, valued, and welcomed. What they found here was not just a service, but a family.</p>
        <p style="margin-top:7px">This is what we are building together.</p>
        <p style="margin-top:7px">These gifts help build momentum, inspire others, and move the vision forward in powerful ways.</p>
      </div>
    </div>
    <div class="photo" role="img" aria-label="Photo of a worship leader singing on a dark stage" style="left:215px;top:245px;width:110px;height:170px;background:radial-gradient(ellipse at 60% 70%,#2f6b5a 0%,#1c2a25 35%,#0d0f0e 75%);border-bottom-left-radius:22px"></div>
    <div class="footer-band">
      <div class="contact-line" style="position:static;color:#fff">
        <span class="contact-phone"><svg width="10" height="10" viewBox="0 0 24 24"><path d="M6.6 10.8a15 15 0 006.6 6.6l2.2-2.2a1 1 0 011-.25 11.4 11.4 0 003.6.6 1 1 0 011 1V20a1 1 0 01-1 1A17 17 0 013 4a1 1 0 011-1h3.5a1 1 0 011 1c0 1.25.2 2.45.6 3.6a1 1 0 01-.25 1z" fill="#fff"/></svg>555.014.2290</span>
        <span class="contact-web"><svg width="9" height="9" viewBox="0 0 24 24" fill="none" stroke="#fff" stroke-width="2"><circle cx="12" cy="12" r="10"/><path d="M2 12h20M12 2c3 3 3 17 0 20M12 2c-3 3-3 17 0 20"/></svg>www.meadowlight-church.org</span>
      </div>
    </div>
  </div>

  <div class="panel panel-inside-right" style="background:#fbf3f3">
    <div class="photo" role="img" aria-label="Faded photo of a cathedral interior with flowers" style="left:0;top:0;width:325px;height:435px;background:linear-gradient(180deg,#e6dcd8 0%,#f3ebea 30%,#f6e6e6 60%,#f1dcdc 100%)"></div>
    <div class="section-title abs" style="left:0;top:15px;width:325px">How We Move Forward Together</div>
    <div class="abs" style="left:0;top:35px;width:325px;text-align:center;font-size:6.3px;font-weight:700">We encourage</div>
    <div class="abs body-text" style="left:30px;top:51px;width:265px;text-align:center">Everyone to participate, even one dollar a day matters Some to give stretch gifts as they are able A few to provide leadership gifts to help anchor the campaign</div>
    <div class="abs" style="left:0;top:80px;width:162px;height:90px;background:var(--charcoal);padding:6px 15px 0;color:#ddd">
      <div style="font-family:'Poppins',sans-serif;font-weight:600;color:var(--brand-red);font-size:11px;line-height:1">A Shared<br>Commitment</div>
      <div class="body-text" style="margin-top:6px">“If each of us gave just $20 a week, we would not only meet our goal, we would exceed it. But this is not about equal giving. It is about equal sacrifice. Some can give more, some less, but together, we can do something powerful.”</div>
    </div>
    <div class="abs" style="left:162px;top:80px;width:163px;height:90px;background:var(--blush);padding:6px 16px 0">
      <div style="font-family:'Poppins',sans-serif;font-weight:600;color:var(--brand-red);font-size:11px">Join Us</div>
      <ul class="bullets" style="margin-top:4px"><li>Pray</li><li>Listen</li><li>Step forward in faith</li></ul>
      <div class="body-text" style="margin-top:4px">Together, we believe God will do more than we can ask or imagine.</div>
    </div>
    <div class="section-title abs" style="left:0;top:180px;width:325px">Realistic Participation Model</div>
    <div class="abs" style="left:0;top:197px;width:325px;text-align:center;font-size:6.3px;font-weight:600">Not everyone will give equally so let’s build a real-world scenario:</div>
    <div class="abs" style="left:0;top:216px;width:325px;text-align:center;font-family:'Poppins',sans-serif;font-weight:600;font-size:9.5px">Tiered Giving Plan</div>
    <table class="tiers abs" style="left:14px;top:237px">
      <tr><th>Group</th><th>People</th><th>Weekly Gift</th><th>Yearly Total</th></tr>
      <tr><td>Leadership<br>Givers</td><td>10</td><td>$100</td><td>$52,000</td></tr>
      <tr><td>Core<br>Givers</td><td>40</td><td>$40</td><td>$38,200</td></tr>
      <tr><td>Consistent<br>Givers</td><td>60</td><td>$20</td><td>$62,400</td></tr>
      <tr><td>Entry<br>Givers</td><td>40</td><td>$10</td><td>$20,800</td></tr>
    </table>
    <div class="abs" style="left:0;top:381px;width:325px;text-align:center;font-family:'Poppins',sans-serif;font-weight:600;font-size:11px">Total: <span class="red">$218,400</span></div>
    <div class="abs" style="left:0;top:398px;width:325px;text-align:center;font-size:6.3px;font-weight:600">This exceeds the goal, giving margin for:</div>
    <ul class="bullets abs" style="left:55px;top:410px;display:flex;gap:12px"><li>Missed weeks</li><li>Lower participation</li><li>Unexpected needs</li></ul>
    <div class="footer-band">
      <div class="contact-line" style="position:static;color:#fff">
        <span class="contact-phone"><svg width="10" height="10" viewBox="0 0 24 24"><path d="M6.6 10.8a15 15 0 006.6 6.6l2.2-2.2a1 1 0 011-.25 11.4 11.4 0 003.6.6 1 1 0 011 1V20a1 1 0 01-1 1A17 17 0 013 4a1 1 0 011-1h3.5a1 1 0 011 1c0 1.25.2 2.45.6 3.6a1 1 0 01-.25 1z" fill="#fff"/></svg>555.014.2290</span>
        <span class="contact-web"><svg width="9" height="9" viewBox="0 0 24 24" fill="none" stroke="#fff" stroke-width="2"><circle cx="12" cy="12" r="10"/><path d="M2 12h20M12 2c3 3 3 17 0 20M12 2c-3 3-3 17 0 20"/></svg>www.meadowlight-church.org</span>
      </div>
    </div>
  </div>
</section>

</body>
</html>
```